Business Card Design Project

looking for business cards with new logo

I am looking to keep with the colors of the logo i posted.  Here are some other details to consider.  I would like my website prominently displayed on the business card with the logo.  my website is www.PRopelVK.com...it should be spelled this way.

My contact information is:

Daniel J Whitcombe III
Broker/Owner
4587 Larkspur Ave., Suite 308
Cedarbrook, Oregon 97321
Office: 830-419-5576
Email:  Daniel@PRopelVK.com

Thank you
Daniel Whitcombe

```html
<!DOCTYPE html>
<html lang="en">
<head>
<meta charset="utf-8">
<title>Propel Realty – Business Card</title>
<link href="https://fonts.googleapis.com/css2?family=Nanum+Gothic:wght@400;700&family=Didact+Gothic&display=swap" rel="stylesheet">
<style>
  :root {
    --backdrop: #2b2b2b;
    --card-navy: #143f6e;
    --card-navy-light: #1c4b7e;
    --accent-blue: #45a9d8;
    --text-white: #ffffff;
    --text-soft: #e6edf5;
  }
  * { margin: 0; padding: 0; box-sizing: border-box; }
  html, body {
    width: 1200px; height: 1000px; overflow: hidden;
    background: var(--backdrop);
    font-family: "Nanum Gothic", Arial, sans-serif;
  }
  .card {
    position: absolute;
    width: 718px; height: 392px;
    background: var(--card-navy);
    box-shadow: 0 6px 18px rgba(0,0,0,0.55);
    overflow: hidden;
  }
  .card-front { left: 241px; top: 86px; }
  .card-back { left: 242px; top: 528px; }

  .name-panel {
    position: absolute; left: 0; top: 60px; width: 262px; height: 260px;
    background: radial-gradient(ellipse at 60% 50%, var(--card-navy-light) 0%, var(--card-navy) 70%);
  }
  .panel-divider {
    position: absolute; left: 260px; top: 64px; width: 4px; height: 256px;
    background: linear-gradient(to bottom, rgba(8,28,52,0), rgba(8,28,52,0.85) 50%, rgba(8,28,52,0));
    filter: blur(1px);
  }
  .person-name {
    position: absolute; left: 39px; top: 176px;
    font-size: 16.5px; font-weight: 700; color: var(--text-white);
  }
  .person-title {
    position: absolute; left: 39px; top: 198px;
    font-size: 11.5px; color: var(--accent-blue); letter-spacing: 0.2px;
  }
  .contact-list { position: absolute; left: 284px; top: 153px; list-style: none; }
  .contact-item {
    display: flex; align-items: center; height: 29px;
    font-size: 13.5px; color: var(--text-soft);
  }
  .contact-icon { width: 22px; height: 16px; margin-right: 15px; fill: var(--text-white); }

  .brand {
    position: absolute; display: flex; align-items: center; color: var(--text-white);
    font-weight: 400; white-space: nowrap;
  }
  .brand-mark { background: var(--accent-blue); flex: none; }
  .brand-front { right: 30px; top: 48px; font-size: 33px; gap: 12px; }
  .brand-front .brand-mark { width: 22px; height: 22px; }
  .brand-back { left: 0; right: 0; top: 168px; justify-content: center; font-size: 52px; gap: 18px; }
  .brand-back .brand-mark { width: 32px; height: 32px; }

  .footer-band {
    position: absolute; left: 0; bottom: 0; width: 482px; height: 21px;
    background: var(--accent-blue);
  }
  .footer-web {
    position: absolute; right: 0; bottom: 0; width: 224px; height: 21px;
    background: var(--accent-blue); color: var(--text-white);
    font-family: "Didact Gothic", Arial, sans-serif; font-size: 15px;
    display: flex; align-items: center; justify-content: center; letter-spacing: 0.6px;
  }
  .back-web {
    position: absolute; right: 15px; bottom: 10px; color: var(--text-white);
    font-family: "Didact Gothic", Arial, sans-serif; font-size: 15.5px; letter-spacing: 0.6px;
  }
</style>
</head>
<body>

<section class="card card-front">
  <div class="brand brand-front"><span class="brand-mark"></span>Propel Realty</div>

  <div class="name-panel"></div>
  <div class="panel-divider"></div>
  <p class="person-name">Daniel J Whitcombe III</p>
  <p class="person-title">BROKER/OWNER</p>

  <ul class="contact-list">
    <li class="contact-item">
      <svg class="contact-icon" viewBox="0 0 22 16" aria-hidden="true">
        <path d="M1 5 Q11 -1 21 5 L19 8 L15 6.5 L15 4.5 Q11 3 7 4.5 L7 6.5 L3 8 Z"/>
        <rect x="4" y="9" width="14" height="6" rx="1"/>
      </svg>830-419-5576
    </li>
    <li class="contact-item">
      <svg class="contact-icon" viewBox="0 0 22 16" aria-hidden="true">
        <path d="M11 0 C7.5 0 5.5 2.5 5.5 5.3 C5.5 9 11 16 11 16 C11 16 16.5 9 16.5 5.3 C16.5 2.5 14.5 0 11 0 Z M11 3 A2.3 2.3 0 1 1 11 7.6 A2.3 2.3 0 1 1 11 3 Z"/>
      </svg>4587 Larkspur Ave., Suite 308 Cedarbrook, Oregon 97321
    </li>
    <li class="contact-item">
      <svg class="contact-icon" viewBox="0 0 22 16" aria-hidden="true">
        <path d="M1 2 H21 V14 H1 Z M2.5 3.5 L11 9.5 L19.5 3.5" fill="none" stroke="#fff" stroke-width="1.5"/>
      </svg>Daniel@PRopelVK.com
    </li>
  </ul>

  <div class="footer-band"></div>
  <div class="footer-web">www.PRopelVK.com</div>
</section>

<section class="card card-back">
  <div class="brand brand-back"><span class="brand-mark"></span>Propel Realty</div>
  <p class="back-web">www.PRopelVK.com</p>
</section>

</body>
</html>
```